New Packaging Design Project

Wine packaging redesign. Retail partner requested a redesign of a private label wine. The old label is attached. Our partner liked the Lantern and Briar label and wanted something similar. There will be a logo added to the top of the label

Went on vacation/holiday

```html
<!DOCTYPE html>
<html lang="en">
<head>
<meta charset="utf-8">
<title>Alder Ridge Red Blend – Label Pair</title>
<link href="https://fonts.googleapis.com/css2?family=Cormorant+Garamond:wght@500&display=swap" rel="stylesheet">
<style>
  :root {
    --backdrop: #d6d6d6;
    --gold: #c9a43a;
    --gold-soft: #b89a4e;
    --night-label: #3e3e3e;
    --night-ridge: #2e2e2e;
    --night-base: #262626;
    --night-waves: #4a4a4a;
    --stone-label: #cbc5b8;
    --stone-ridge: #7f786d;
    --stone-base: #6e685e;
    --stone-waves: #8d877c;
  }
  * { box-sizing: border-box; margin: 0; padding: 0; }
  html, body { width: 1200px; height: 898px; overflow: hidden; }
  body {
    background: var(--backdrop);
    display: flex;
    align-items: center;
    justify-content: center;
    gap: 64px;
  }
  .wine-label {
    position: relative;
    width: 300px;
    height: 464px;
    overflow: hidden;
    text-align: center;
    font-family: "Cormorant Garamond", serif;
    font-weight: 500;
  }
  .wine-label--night { background: var(--night-label); --ridge: var(--night-ridge); --base: var(--night-base); --waves: var(--night-waves); --sub: var(--gold); }
  .wine-label--stone { background: var(--stone-label); --ridge: var(--stone-ridge); --base: var(--stone-base); --waves: var(--stone-waves); --sub: var(--gold-soft); }

  .wine-label__name {
    position: absolute; top: 92px; left: 0; right: 0;
    font-size: 30px; line-height: 1;
    font-weight: 500;
    letter-spacing: 1px;
    color: var(--gold);
  }
  .wine-label__style {
    position: absolute; top: 134px; left: 0; right: 0;
    font-size: 15px; letter-spacing: 1px;
    color: var(--sub);
  }
  .wine-label__ridge {
    position: absolute; top: 178px; left: 0; right: 0; height: 152px;
    background: linear-gradient(180deg, transparent 0%, var(--ridge) 30%, var(--base) 100%);
  }
  .wine-label__varietals {
    position: absolute; top: 272px; left: 0; right: 0;
    color: var(--sub);
  }
  .wine-label__varietal--minor { display: block; font-size: 13px; letter-spacing: 0.5px; }
  .wine-label__varietal--major { display: block; font-size: 17px; letter-spacing: 0.5px; margin-top: 6px; }
  .wine-label__waves {
    position: absolute; top: 330px; left: 0; right: 0; height: 104px;
    background: linear-gradient(180deg, var(--waves), var(--base));
  }
  .wine-label__foot {
    position: absolute; top: 434px; left: 0; right: 0; bottom: 0;
    background: var(--base);
  }
  .wine-label__vintage {
    position: absolute; bottom: 10px; left: 0; right: 0;
    font-size: 11px; letter-spacing: 1px;
    color: var(--sub);
  }
</style>
</head>
<body>
  <section class="wine-label wine-label--night">
    <div class="wine-label__ridge" role="img" aria-label="Mountain silhouette illustration"></div>
    <div class="wine-label__waves" role="img" aria-label="Hatched ocean wave illustration"></div>
    <div class="wine-label__foot"></div>
    <h1 class="wine-label__name">ALDER RIDGE</h1>
    <p class="wine-label__style">RED BLEND</p>
    <p class="wine-label__varietals">
      <span class="wine-label__varietal--minor">PETIT VERDO</span>
      <span class="wine-label__varietal--major">CABERNET SAUVIGNON</span>
    </p>
    <p class="wine-label__vintage">2018</p>
  </section>

  <section class="wine-label wine-label--stone">
    <div class="wine-label__ridge" role="img" aria-label="Mountain silhouette illustration"></div>
    <div class="wine-label__waves" role="img" aria-label="Hatched ocean wave illustration"></div>
    <div class="wine-label__foot"></div>
    <h1 class="wine-label__name">ALDER RIDGE</h1>
    <p class="wine-label__style">RED BLEND</p>
    <p class="wine-label__varietals">
      <span class="wine-label__varietal--minor">PETIT VERDO</span>
      <span class="wine-label__varietal--major">CABERNET SAUVIGNON</span>
    </p>
    <p class="wine-label__vintage">2018</p>
  </section>
</body>
</html>
```